Simple Business Card Design

Professional/clean business card with custom logo included in layout.

Target Market(s)

N/A

Industry/Entity Type

Business

Contact Information for Business Card

Name: Marlene Hoskin, PT; NV Medicaid Provider; Phone: (775) 918-2467; Toll-free phone: (877) 406-1953; email: mar@copperfieldlaneventuresltd.example

Font styles to use
Serif
Decorative
Script

Requirements
Must have
• See "details" above.
Nice to have
• Would be interested to see dark vs. light/grayscale backgrounds that accentuate/contrast the logo colors. (I.e. dark navy background w/ white or grey text, etc.)

```html
<!DOCTYPE html>
<html lang="en">
<head>
<meta charset="utf-8">
<title>Copperfield Lane Ventures — Business Card</title>
<link rel="stylesheet" href="https://fonts.googleapis.com/css2?family=EB+Garamond:wght@400;600&display=swap">
<style>
  :root {
    --page-bg: #e9e6e1;
    --card-navy: #1c2f6e;
    --card-deep: #0b1538;
    --card-black: #020308;
    --text-light: #f1f1f4;
    --mark-grey: #b9bcc6;
    --mark-copper: #e0673a;
  }
  * { box-sizing: border-box; margin: 0; padding: 0; }
  html, body {
    width: 1200px;
    height: 900px;
    overflow: hidden;
    background: var(--page-bg);
  }
  .canvas {
    width: 1200px;
    height: 900px;
    display: flex;
    align-items: center;
    justify-content: center;
  }
  .business-card {
    position: relative;
    width: 840px;
    height: 480px;
    background:
      radial-gradient(ellipse 70% 75% at 42% 30%, var(--card-navy) 0%, var(--card-deep) 55%, var(--card-black) 100%);
    box-shadow: 0 18px 40px rgba(0, 0, 0, 0.25);
    font-family: "EB Garamond", "Times New Roman", serif;
    color: var(--text-light);
  }
  .brand {
    position: absolute;
    top: 58px;
    right: 52px;
    display: flex;
    align-items: center;
    gap: 16px;
  }
  .brand-dot {
    width: 62px;
    height: 62px;
    border-radius: 50%;
    background: var(--mark-copper);
  }
  .brand-name {
    font-size: 30px;
    font-weight: 600;
    line-height: 1.05;
    color: var(--mark-grey);
    letter-spacing: 0.02em;
  }
  .contact {
    position: absolute;
    right: 48px;
    bottom: 64px;
    text-align: right;
    font-size: 24px;
    line-height: 1.32;
  }
  .contact-line {
    display: flex;
    justify-content: flex-end;
    align-items: center;
    gap: 8px;
    white-space: nowrap;
  }
  .contact-icon {
    width: 20px;
    height: 20px;
    flex: none;
  }
</style>
</head>
<body>
<main class="canvas">
  <section class="business-card" aria-label="Business card for Copperfield Lane Ventures, Ltd.">
    <div class="brand">
      <span class="brand-dot" aria-hidden="true"></span>
      <div class="brand-name">Copperfield Lane<br>Ventures, Ltd.</div>
    </div>

    <address class="contact">
      <p class="contact-line">Marlene Hoskin, PT; NV Medicaid Provider;</p>
      <p class="contact-line">
        <svg class="contact-icon" viewBox="0 0 20 20" aria-label="Phone">
          <rect x="6" y="2" width="8" height="16" rx="1.5" fill="none" stroke="#f1f1f4" stroke-width="1.5"/>
          <rect x="7.5" y="4.5" width="5" height="5" fill="#f1f1f4"/>
          <circle cx="10" cy="14.5" r="1" fill="#f1f1f4"/>
        </svg>
        (775) 918-2467; Toll-free phone: (877) 406-1953;
      </p>
      <p class="contact-line">
        <svg class="contact-icon" viewBox="0 0 20 20" aria-label="Email">
          <rect x="2" y="5" width="16" height="11" fill="none" stroke="#f1f1f4" stroke-width="1.5"/>
          <path d="M2 5 L10 11 L18 5" fill="none" stroke="#f1f1f4" stroke-width="1.5"/>
        </svg>
        mar@copperfieldlaneventuresltd.example
      </p>
    </address>
  </section>
</main>
</body>
</html>
```